Restyle corporate identity (+ logo) for a road construction company

We need a new logo and stationary design for our company VELMOR path. VELMOR path® increases the road base strength, while reducing major costs and time of road construction. Attached some examples of the current design.

Our wishes for the new logo:
- Business look
- Style sheet
- Modern

More information: www.velmorpath-example.com
Updates

Target Market(s)

Government

Industry/Entity Type

Construction

Requirements
Must have
• Logo (with road sign) + text

```html
<!DOCTYPE html>
<html lang="en">
<head>
<meta charset="utf-8">
<title>VELMOR path – Business Card</title>
<link rel="stylesheet" href="https://fonts.googleapis.com/css2?family=Dosis:wght@600&family=PT+Sans:wght@400;700&display=swap">
<style>
  :root {
    --brand-blue: #0f7be0;
    --brand-blue-dark: #0a6ccc;
    --ink: #3a3a3a;
    --muted: #8a8a8a;
    --rule: #4a5a78;
    --band-grey: #a6a6a6;
    --paper: #ebebed;
    --backdrop: #8e8e8e;
    --white: #ffffff;
  }
  * { box-sizing: border-box; margin: 0; padding: 0; }
  html, body {
    width: 1105px; height: 1200px; overflow: hidden;
    background: var(--backdrop);
  }
  .card {
    position: absolute; left: 180px;
    width: 745px; height: 427px;
    overflow: hidden;
  }
  .card--front { top: 90px; background: var(--paper); }
  .card--back { top: 640px; background: var(--brand-blue); }

  /* Front */
  .brand {
    position: absolute; left: 47px; top: 56px;
    display: flex; align-items: center; gap: 16px;
  }
  .brand__mark {
    width: 62px; height: 98px; border-radius: 12px;
    background: var(--brand-blue);
  }
  .brand__name {
    font-family: "Dosis", sans-serif; font-weight: 600;
    color: var(--brand-blue); line-height: 0.92;
  }
  .brand__name span { display: block; }
  .brand__name .line-1 { font-size: 58px; letter-spacing: 1px; }
  .brand__name .line-2 { font-size: 46px; letter-spacing: 14px; }

  .holder {
    position: absolute; right: 44px; top: 218px; text-align: right;
    font-family: "PT Sans", sans-serif;
  }
  .holder__name { font-size: 25px; font-weight: 700; color: var(--brand-blue); letter-spacing: 0.5px; line-height: 1.1; }
  .holder__role { font-size: 19px; color: var(--muted); line-height: 1.3; }
  .holder-tab {
    position: absolute; left: 729px; top: 224px;
    width: 16px; height: 54px; background: var(--brand-blue);
  }
  .divider {
    position: absolute; left: 47px; top: 290px;
    width: 654px; height: 1px; background: var(--rule);
  }
  .contact {
    position: absolute; top: 302px;
    font-family: "PT Sans", sans-serif; font-size: 19px;
    color: var(--ink); line-height: 27.5px; list-style: none;
  }
  .contact--digital { left: 47px; }
  .contact--address { right: 44px; text-align: right; }
  .contact li { display: flex; align-items: center; gap: 9px; }
  .contact--address li { display: block; }
  .contact svg { width: 17px; height: 17px; fill: var(--brand-blue); flex: none; }

  .footer-band {
    position: absolute; left: 0; bottom: 0;
    width: 745px; height: 12px;
  }

  /* Back */
  .back-brand {
    position: absolute; right: 55px; top: 228px; text-align: right;
    font-family: "Dosis", sans-serif; font-weight: 600;
    color: var(--white); line-height: 0.95;
  }
  .back-brand span { display: block; }
  .back-brand .line-1 { font-size: 82px; letter-spacing: 1px; }
  .back-brand .line-2 { font-size: 62px; letter-spacing: 22px; margin-right: -22px; }
  .back-url {
    position: absolute; right: 55px; top: 362px;
    font-family: "PT Sans", sans-serif; font-size: 20px;
    color: var(--white); letter-spacing: 1.5px;
  }
</style>
</head>
<body>

<section class="card card--front" aria-label="Business card front">
  <div class="brand">
    <div class="brand__mark"></div>
    <div class="brand__name"><span class="line-1">VELMOR</span><span class="line-2">PATH</span></div>
  </div>

  <div class="holder">
    <p class="holder__name">DAAN VERHOEF</p>
    <p class="holder__role">CEO/Founder</p>
  </div>
  <div class="holder-tab"></div>
  <div class="divider"></div>

  <ul class="contact contact--digital">
    <li>
      <svg viewBox="0 0 24 24" aria-hidden="true"><path d="M6.6 10.8a15.1 15.1 0 0 0 6.6 6.6l2.2-2.2c.3-.3.7-.4 1-.2 1.1.4 2.3.6 3.6.6.6 0 1 .4 1 1V20c0 .6-.4 1-1 1A17 17 0 0 1 3 4c0-.6.4-1 1-1h3.5c.6 0 1 .4 1 1 0 1.3.2 2.5.6 3.6.1.3 0 .7-.2 1z"/></svg>
      612 555 0184
    </li>
    <li>
      <svg viewBox="0 0 24 24" aria-hidden="true"><path d="M2 5h20v14H2z M3.5 6.5 12 12.5l8.5-6z" fill-rule="evenodd"/></svg>
      contact@velmorpath-example.com
    </li>
    <li>
      <svg viewBox="0 0 24 24" aria-hidden="true"><circle cx="12" cy="12" r="10"/><path d="M2 12h20M12 2c3 3 3 17 0 20M12 2c-3 3-3 17 0 20" stroke="#ebebed" stroke-width="1.6" fill="none"/></svg>
      www.velmorpath-example.com
    </li>
  </ul>

  <ul class="contact contact--address">
    <li>Havenstraat 88</li>
    <li>3011 XL Rotterdam</li>
    <li>The Netherlands</li>
  </ul>

  <svg class="footer-band" viewBox="0 0 745 12" preserveAspectRatio="none" aria-hidden="true">
    <polygon points="0,0 490,0 484,12 0,12" fill="var(--brand-blue)"/>
    <polygon points="496,0 745,0 745,12 490,12" fill="var(--band-grey)"/>
  </svg>
</section>

<section class="card card--back" aria-label="Business card back">
  <div class="back-brand"><span class="line-1">VELMOR</span><span class="line-2">PATH</span></div>
  <p class="back-url">www.velmorpath-example.com</p>
</section>

</body>
</html>
```